Business Card Design Project

Use our current logo. Clean design.

Industry/Entity Type

Business

Requirements
Must have
• Marisela DUBRANCQ
M. Law
Managing Partner

Alpenvorsa AG
Kornhalmweg 214
CH-3097 Liebefeld

M. +41 79 412 56 27
T. +41 31 928 44 10
F. +41 31 928 44 19

m.dubrancq@alpenvorsa-example.com
www.alpenvorsa-example.com

```html
<!DOCTYPE html>
<html lang="en">
<head>
<meta charset="utf-8">
<title>Alpenvorsa business card</title>
<link rel="stylesheet" href="https://fonts.googleapis.com/css2?family=Noto+Sans:wght@400;600;700&display=swap">
<style>
  :root {
    --page-bg: #ecebe8;
    --card-bg: #ffffff;
    --ink: #1c1a1a;
    --rule: #9a9a9a;
    --icon: #8e8e8e;
    --card-edge: #d9d9d9;
  }
  * { margin: 0; padding: 0; box-sizing: border-box; }
  html, body { width: 1200px; height: 1000px; overflow: hidden; }
  body {
    background: var(--page-bg);
    font-family: "Noto Sans", Verdana, sans-serif;
    color: var(--ink);
    position: relative;
  }
  .card {
    position: absolute;
    background: var(--card-bg);
    border: 1px solid var(--card-edge);
    box-shadow: 0 3px 8px rgba(0,0,0,0.18);
    overflow: hidden;
  }
  .card-back { left: 256px; top: 66px; width: 728px; height: 414px; }
  .card-front { left: 73px; top: 440px; width: 729px; height: 417px; }

  .back-rule {
    position: absolute; left: 0; right: 0; height: 1px; background: var(--rule);
  }
  .back-rule.upper { top: 118px; }
  .back-rule.lower { top: 296px; }
  .brand {
    position: absolute; left: 0; right: 0; top: 178px;
    display: flex; justify-content: center; align-items: center; gap: 12px;
  }
  .brand-mark { width: 16px; height: 16px; background: var(--ink); }
  .brand-name { font-size: 30px; font-weight: 400; letter-spacing: 1px; }

  .holder {
    position: absolute; left: 0; width: 730px; top: 70px; text-align: center;
  }
  .holder-name { font-size: 22px; font-weight: 700; letter-spacing: 0.3px; }
  .holder-rule { width: 180px; height: 1px; margin: 4px auto 6px; background: var(--rule); }
  .holder-role { font-size: 20px; font-weight: 400; letter-spacing: 0.4px; }

  .contacts { position: absolute; top: 257px; font-size: 13.5px; letter-spacing: 0.5px; }
  .contacts.phones { left: 120px; }
  .contacts.online { left: 360px; top: 282px; }
  .contact { display: flex; align-items: center; height: 26px; }
  .contact svg { width: 22px; height: 18px; margin-right: 12px; fill: var(--icon); }

  .address {
    position: absolute; left: 115px; top: 373px;
    font-size: 11px; letter-spacing: 3.2px;
  }
</style>
</head>
<body>
  <section class="card card-back" aria-label="Card back">
    <div class="back-rule upper"></div>
    <div class="brand">
      <span class="brand-mark"></span>
      <span class="brand-name">ALPENVORSA</span>
    </div>
    <div class="back-rule lower"></div>
  </section>

  <section class="card card-front" aria-label="Card front">
    <div class="holder">
      <div class="holder-name">Marisela DUBRANCQ M. Law</div>
      <div class="holder-rule"></div>
      <div class="holder-role">Managing Partner</div>
    </div>

    <div class="contacts phones">
      <div class="contact">
        <svg viewBox="0 0 22 18" aria-hidden="true"><rect x="6" y="0" width="10" height="18" rx="2"/><rect x="8" y="2" width="6" height="11" fill="#fff"/></svg>
        <span>+41 79 412 56 27</span>
      </div>
      <div class="contact">
        <svg viewBox="0 0 22 18" aria-hidden="true"><path d="M5 1 L9 1 L10 5 L8 7 Q10 11 13 12 L15 10 L19 11 L19 15 Q17 17 14 16 Q6 13 4 5 Q4 2 5 1 Z"/></svg>
        <span>+41 31 928 44 10</span>
      </div>
      <div class="contact">
        <svg viewBox="0 0 22 18" aria-hidden="true"><rect x="6" y="1" width="10" height="6"/><rect x="1" y="6" width="20" height="9" rx="2"/><rect x="5" y="12" width="12" height="6" fill="#bbb"/></svg>
        <span>+41 31 928 44 19</span>
      </div>
    </div>

    <div class="contacts online">
      <div class="contact">
        <svg viewBox="0 0 22 18" aria-hidden="true"><rect x="1" y="2" width="20" height="14" rx="3"/><path d="M4 9 H18 M11 4 V14" stroke="#fff" stroke-width="1"/></svg>
        <span>alpenvorsa-example.com</span>
      </div>
      <div class="contact">
        <svg viewBox="0 0 22 18" aria-hidden="true"><rect x="1" y="3" width="20" height="12" rx="1"/><path d="M1 4 L11 11 L21 4" stroke="#fff" stroke-width="1.2" fill="none"/></svg>
        <span>m.dubrancq@alpenvorsa-example.com</span>
      </div>
    </div>

    <div class="address">Alpenvorsa AG Kornhalmweg 214 CH-3097 Liebefeld</div>
  </section>
</body>
</html>
```